Brochure for services and brand overview of new agency

With the recent launch of a new brand and business strategy agency, I am looking for a 2-3 page digital brochure that I can attach to emails as I open the dialogue with potential clients. This brochure has to fall in line with our brand...modern and sleek, with a highly professional look and feel. The content can come from a combination of our website (www.quillbarn.co) and any additional content can come from you or just ask me to provide. Logos and other materials are provided as well. I have also included a sample of one of my other brochures from another company I own, just so you can get an example of the quality and feel I like.

Target Market(s)

Divorce Professionals (Attorneys, Mediators, Therapists, etc)

Industry/Entity Type

Agency

Font styles to use
Serif

Requirements
Must have
• High end brand feel.
Specific content with relation to services, brand ethos, etc....with a subtle call to action.
Should not have
• Hard Sales Language
Cheap looking stock photos

Don't go too heavy in written content. Just scratch the surface in a way that will capture attention and get them to want to call. It's more about the design and inspirational aspects of it.

```html
<!DOCTYPE html>
<html lang="en">
<head>
<meta charset="utf-8">
<title>Quillbarn Agency – Brochure</title>
<link href="https://fonts.googleapis.com/css2?family=Montserrat:wght@300;400;500;700;800&display=swap" rel="stylesheet">
<style>
  :root {
    --crimson: #a8003a;
    --ink: #1f1f22;
    --paper: #f4f4f8;
    --text: #3a3a40;
    --contact-text: #e6e6ea;
    --backdrop: #6b6b6b;
  }
  * { margin: 0; padding: 0; box-sizing: border-box; }
  html, body { width: 1200px; height: 789px; overflow: hidden; }
  body {
    background: var(--backdrop);
    font-family: "Montserrat", sans-serif;
    color: var(--text);
    position: relative;
  }
  .page {
    position: absolute;
    top: 15px;
    width: 537px;
    height: 759px;
    background: var(--paper);
    overflow: hidden;
  }
  .page--back { left: 63px; }
  .page--front { left: 600px; box-shadow: inset 6px 0 10px -6px rgba(0,0,0,.18); }

  /* Back page */
  .contact-band {
    position: absolute; inset: 0;
    background: var(--ink);
    clip-path: polygon(0 76%, 100% 62%, 100% 100%, 0 100%);
  }
  .about { position: absolute; left: 40px; top: 96px; width: 200px; }
  .about__title {
    font-size: 19px; font-weight: 300; color: var(--ink);
    letter-spacing: .5px; padding-bottom: 6px;
    border-bottom: 1.5px solid var(--crimson);
    white-space: nowrap;
  }
  .about__title strong { font-weight: 800; color: var(--crimson); }
  .about__text { font-size: 7.4px; line-height: 1.5; margin-top: 14px; text-align: justify; }
  .about__text + .about__text { margin-top: 10px; }

  .team-photo { position: absolute; left: 250px; top: 92px; }

  .social { position: absolute; right: 40px; top: 450px; display: flex; gap: 6px; }
  .social__dot { width: 22px; height: 22px; border-radius: 50%; background: var(--ink); }

  .contact__tag {
    position: absolute; left: 92px; top: 570px;
    background: var(--crimson); color: #fff;
    font-size: 17px; font-weight: 300; padding: 6px 18px 6px 22px; letter-spacing: .5px;
  }
  .contact__tag strong { font-weight: 700; }
  .contact__list { position: absolute; left: 96px; top: 620px; list-style: none; }
  .contact__item {
    display: flex; align-items: flex-start; gap: 12px;
    color: var(--contact-text); font-size: 10px; font-weight: 300; line-height: 1.45; margin-bottom: 9px;
  }
  .contact__item svg { flex: none; margin-top: 2px; }

  /* Front page */
  .brand { position: absolute; left: 0; right: 0; top: 56px; text-align: center; color: var(--ink); }
  .brand__name { font-size: 38px; font-weight: 400; letter-spacing: -.5px; line-height: 1; }
  .brand__sub { font-size: 8px; font-weight: 400; letter-spacing: 4px; margin-top: 4px; padding-left: 120px; }

  .cover-art { position: absolute; left: 45px; top: 150px; }
  .cover-title { position: absolute; left: 130px; top: 330px; color: #fff; line-height: .95; }
  .cover-title__bold { font-size: 58px; font-weight: 800; letter-spacing: 1px; display: block; }
  .cover-title__light { font-size: 52px; font-weight: 300; letter-spacing: 1px; display: block; }

  .cover-url {
    position: absolute; left: 0; right: 0; top: 690px; text-align: center;
    font-size: 11px; font-weight: 500; letter-spacing: 4px; color: var(--ink);
  }
  .cover-url span { color: var(--crimson); }
</style>
</head>
<body>

<section class="page page--back">
  <div class="contact-band"></div>

  <div class="about">
    <h2 class="about__title">ABOUT <strong>QUILLBARN</strong></h2>
    <p class="about__text">Our "exclusive to divorce professionals" brand and business strategy agency is designed with intention to provide divorce professionals a way to enhance their market positioning and brand to achieve their most simple and audacious professional goals.</p>
    <p class="about__text">The goal is to provide the tools, resources and services to our clients, giving them the global visibility they need to position themselves as leaders in the field, while also enabling them to create the best divorce experience for end consumer. The result of this strategic positioning is a significant increase of quality client opportunities, providing the opportunity to set them on the right path to a successful outcome.</p>
    <p class="about__text">By breaking down specific elements that require attention and strategically creating an action plan for their business, we provide our clients the tools to help them achieve their personal and professional goals, help position themselves in the industry and create a platform that resonates with their ideal clients. We provide all the systems and strategies, as well as the core fundamentals upon which the company is based.</p>
  </div>

  <svg class="team-photo" width="270" height="270" viewBox="0 0 270 270">
    <defs>
      <radialGradient id="teamTone" cx="50%" cy="45%" r="60%">
        <stop offset="0" stop-color="#7a6a5c"/>
        <stop offset="1" stop-color="#b9b3aa"/>
      </radialGradient>
    </defs>
    <circle cx="135" cy="135" r="112" fill="none" stroke="var(--crimson)" stroke-width="26" stroke-linecap="round" stroke-dasharray="520 200" transform="rotate(-200 135 135)"/>
    <circle cx="135" cy="135" r="90" fill="url(#teamTone)" role="img" aria-label="Photo of a team talking together around desks in an open office"/>
  </svg>

  <div class="social" aria-label="Social channels">
    <span class="social__dot"></span><span class="social__dot"></span><span class="social__dot"></span><span class="social__dot"></span><span class="social__dot"></span>
  </div>

  <div class="contact__tag">CONTACT <strong>US</strong></div>
  <ul class="contact__list">
    <li class="contact__item">
      <svg width="10" height="12" viewBox="0 0 10 12"><path d="M5 11.5S1 7 1 4.5a4 4 0 0 1 8 0C9 7 5 11.5 5 11.5z" fill="none" stroke="var(--crimson)" stroke-width="1.2"/><circle cx="5" cy="4.5" r="1.3" fill="var(--crimson)"/></svg>
      <span>780 Alder Row<br>Crestmoor Bay, CA<br>United States, 90517</span>
    </li>
    <li class="contact__item">
      <svg width="10" height="10" viewBox="0 0 10 10"><path d="M2 1l2 2-1 1.5c.6 1.2 1.3 1.9 2.5 2.5L7 6l2 2-1.5 1.5C4 9 1 6 .5 2.5z" fill="none" stroke="var(--crimson)" stroke-width="1"/></svg>
      <span>+310 555 0187</span>
    </li>
    <li class="contact__item">
      <svg width="11" height="9" viewBox="0 0 11 9"><rect x=".5" y=".5" width="10" height="8" fill="none" stroke="var(--crimson)"/><path d="M.5.5l5 4.5 5-4.5" fill="none" stroke="var(--crimson)"/></svg>
      <span>nora@quillbarn.co</span>
    </li>
    <li class="contact__item">
      <svg width="10" height="10" viewBox="0 0 10 10"><circle cx="5" cy="5" r="4.5" fill="none" stroke="var(--crimson)"/><ellipse cx="5" cy="5" rx="2" ry="4.5" fill="none" stroke="var(--crimson)"/><path d="M.5 5h9" stroke="var(--crimson)"/></svg>
      <span>www.quillbarn.co</span>
    </li>
  </ul>
</section>

<section class="page page--front">
  <header class="brand">
    <div class="brand__name">quillbarn</div>
    <div class="brand__sub">AGENCY</div>
  </header>

  <svg class="cover-art" width="450" height="500" viewBox="0 0 450 500">
    <defs>
      <radialGradient id="blocksTone" cx="55%" cy="55%" r="60%">
        <stop offset="0" stop-color="#4a4a4e"/>
        <stop offset="1" stop-color="#1e1e22"/>
      </radialGradient>
    </defs>
    <circle cx="225" cy="245" r="215" fill="none" stroke="var(--crimson)" stroke-width="56" stroke-linecap="round" stroke-dasharray="1150 200" transform="rotate(-215 225 245)"/>
    <circle cx="225" cy="245" r="178" fill="url(#blocksTone)" role="img" aria-label="Photo of wooden blocks labelled with branding services"/>
  </svg>

  <h1 class="cover-title">
    <span class="cover-title__bold">BRAND</span>
    <span class="cover-title__light">MATTERS</span>
  </h1>

  <p class="cover-url">www.<span>quillbarn</span>.co</p>
</section>

</body>
</html>
```